Side of Page Partnership-type Letterhead Design for Chiropractic Office

Side oriented letterhead with practice locations/demographics, physician names and company logo

Target Market(s)

Healthcare Professionals & Attorneys

Industry/Entity Type

Healthcare

Font styles to use
Other font styles liked:
• Font of Logo is Trajan Pro, but not a deal breaker if we try something else

Colors

Designer to choose colors to be used in the design.

Requirements
Must have
• All info from attached documents

```html
<!DOCTYPE html>
<html lang="en">
<head>
<meta charset="utf-8">
<title>Keystone Chiropractic Letterhead</title>
<link href="https://fonts.googleapis.com/css2?family=Cinzel:wght@400;500&display=swap" rel="stylesheet">
<style>
  :root {
    --backdrop: #2a2d30;
    --page-light: #f4f4f4;
    --page-dark: #dcdcdc;
    --sidebar-light: #dadada;
    --sidebar-dark: #cfcfcf;
    --ink: #1c1c1c;
    --ink-soft: #3a3a3a;
    --brand-blue: #2d3d91;
    --brand-orange: #e0891c;
    --brand-green: #5c9a3c;
  }
  * { box-sizing: border-box; margin: 0; padding: 0; }
  html, body {
    width: 1200px;
    height: 780px;
    overflow: hidden;
    background: var(--backdrop);
  }
  .letterhead {
    position: absolute;
    left: 338px;
    top: 20px;
    width: 523px;
    height: 740px;
    background: linear-gradient(160deg, var(--page-light) 0%, var(--page-dark) 100%);
    font-family: "Cinzel", "Times New Roman", serif;
    color: var(--ink);
    box-shadow: 0 6px 24px rgba(0,0,0,0.45);
  }
  .brand {
    position: absolute;
    left: 25px;
    top: 54px;
    color: var(--ink-soft);
    font-weight: 400;
    line-height: 1;
  }
  .brand-name { display: block; font-size: 21px; letter-spacing: 0.2px; }
  .brand-sub { display: block; font-size: 12.5px; margin-top: 1px; letter-spacing: 0.3px; }
  .sidebar {
    position: absolute;
    left: 0;
    top: 108px;
    width: 163px;
    bottom: 0;
    background: linear-gradient(180deg, var(--sidebar-light) 0%, var(--sidebar-dark) 100%);
  }
  .physicians {
    list-style: none;
    position: absolute;
    left: 25px;
    top: 40px;
    font-size: 9.4px;
    line-height: 16.4px;
    color: var(--ink);
    white-space: nowrap;
  }
  .locations {
    position: absolute;
    left: 24px;
    top: 392px;
    font-size: 8.6px;
    line-height: 11.4px;
    color: var(--ink-soft);
  }
  .location { font-style: normal; }
  .location-name { display: block; }
  .location--north .location-name, .location--north .label { color: var(--brand-blue); }
  .location--east .location-name, .location--east .label { color: var(--brand-orange); }
  .location--south .location-name, .location--south .label { color: var(--brand-green); }
  .divider {
    width: 31px;
    height: 1px;
    background: var(--ink);
    margin: 7px 0 12px;
  }
</style>
</head>
<body>
  <div class="letterhead">
    <div class="brand">
      <span class="brand-name">Keystone</span>
      <span class="brand-sub">Chiropractic</span>
    </div>
    <aside class="sidebar">
      <ul class="physicians">
        <li>Daniel Whitford, DC, DACNB</li>
        <li>Evan Whitford, DC</li>
        <li>Grant Ellison, DC</li>
        <li>Owen Halvorsen, DC</li>
        <li>Miles Corbett, DC</li>
        <li>Lucas Pennington, DC</li>
        <li>Nolan Ashby, DC</li>
      </ul>
      <div class="locations">
        <address class="location location--north">
          <span class="location-name">Brookhaven</span>
          4120 N. Maple St.<br>
          Brookhaven, OH 43001<br>
          <span class="label">P:</span> 555-210-4400<br>
          <span class="label">F:</span> 555-210-4401
        </address>
        <div class="divider"></div>
        <address class="location location--east">
          <span class="location-name">Elmwood</span>
          217 N. Cedar St.<br>
          Elmwood, OH 43002<br>
          <span class="label">P:</span> 555-318-7200<br>
          <span class="label">F:</span> 555-318-7201
        </address>
        <div class="divider"></div>
        <address class="location location--south">
          <span class="location-name">Fairmont</span>
          582 S. Linden Rd<br>
          Fairmont, OH 43003<br>
          <span class="label">P:</span> 555-427-6600<br>
          <span class="label">F:</span> 555-427-6601
        </address>
      </div>
    </aside>
  </div>
</body>
</html>
```